DJ VAZ (POSTER BANNER)

I just added a sketch to make it easier.
Also it is added:
Under the logo a tag line that says:
DJ-SERVICE-RENTALS

The information given is all is needed for the banner.
The banner needs to be horizontally rather than vertical.
The picture provided is more for a reference point rather for it to be the focal point of the banner.
The logo needs to be the focal point. Also, the phone number needs to be big but not bigger than the email address.
The vibe of the banner needs to be very energetic since I primarily do Vorlund events.

Size of banner is 4x8

Colors:
I like that deep blue, deep red, a little black.
I mainly want for it to call attention.

Need a big poster design for an event that I have coming up. I will provide with the logos that unfortunately will have to be recreated because it is in Photoshop.

I'm sending you some items that I think will be needed, but let me know if you need anything else please.

Phone: 555.014.2368
email: DJ@DJVAZ.net

Target Market(s)

Audience form 18-39
I DJ at a lot of Vorlund events and this event is one of them.

Industry/Entity Type

Events

Requirements
Must have
• Needs to be horizontal.
Red color scheme
Nice to have
• Abstract design to complement the logo the overall finish look of the banner
Should not have
• The picture MUST not be the focal point of the design.
The design should be kinda modern. If you want to use illustrations, they need to be related to Vorlund and Turntables (but needs to be limited)
I added some pictures for ideas.
I'm a little more inclined to use the logo without the slogan in it.

```html
<!DOCTYPE html>
<html lang="en">
<head>
<meta charset="utf-8">
<title>DJ VAZ — Banner</title>
<link href="https://fonts.googleapis.com/css2?family=Bebas+Neue&family=Questrial&display=swap" rel="stylesheet">
<style>
  :root {
    --page: #ffffff;
    --night: #0b0f3a;
    --deep-blue: #1a2a8c;
    --glow-blue: #3f6bff;
    --deep-red: #c8161d;
    --hot-red: #ff2a1f;
    --violet: #7a2a9c;
    --ink: #05060f;
    --white: #ffffff;
  }
  html, body {
    margin: 0;
    width: 1200px;
    height: 1000px;
    overflow: hidden;
    background: var(--page);
  }
  .canvas {
    position: relative;
    width: 1200px;
    height: 1000px;
  }
  .banner {
    position: absolute;
    left: 139px;
    top: 270px;
    width: 922px;
    height: 460px;
    overflow: hidden;
    background: var(--night);
  }
  .banner-backdrop {
    position: absolute;
    inset: 0;
    background:
      radial-gradient(ellipse 60% 18% at 50% 22%, rgba(63,107,255,0.55), transparent 70%),
      radial-gradient(ellipse 40% 30% at 8% 30%, rgba(255,42,31,0.55), transparent 70%),
      radial-gradient(ellipse 40% 30% at 95% 28%, rgba(255,42,31,0.5), transparent 70%),
      radial-gradient(ellipse 50% 25% at 50% 2%, rgba(122,42,156,0.7), transparent 70%),
      radial-gradient(ellipse 70% 25% at 50% 100%, rgba(200,22,29,0.45), transparent 70%),
      radial-gradient(ellipse 50% 40% at 50% 60%, rgba(26,42,140,0.6), transparent 75%),
      linear-gradient(180deg, #2a0f4a 0%, var(--night) 45%, #140a2e 100%);
  }
  .turntable-photo {
    position: absolute;
    left: 626px;
    top: 330px;
    width: 296px;
    height: 130px;
    background:
      radial-gradient(ellipse 40% 45% at 75% 80%, rgba(230,40,30,0.9), transparent 75%),
      radial-gradient(ellipse 25% 20% at 20% 15%, rgba(220,40,30,0.8), transparent 75%),
      linear-gradient(160deg, #3a3d48 0%, #1b1c24 60%, #2a1416 100%);
    border-top-left-radius: 40px;
  }
  .logo-name {
    position: absolute;
    left: 0;
    width: 100%;
    top: 36px;
    text-align: center;
    font-family: "Bebas Neue", sans-serif;
    font-size: 136px;
    line-height: 1;
    letter-spacing: 34px;
    padding-left: 34px;
    box-sizing: border-box;
    color: var(--white);
  }
  .tagline {
    position: absolute;
    left: 0;
    width: 100%;
    top: 196px;
    text-align: center;
    font-family: "Bebas Neue", sans-serif;
    font-size: 60px;
    line-height: 1;
    color: var(--deep-red);
    letter-spacing: 1px;
  }
  .contact {
    position: absolute;
    display: flex;
    align-items: center;
    font-family: "Questrial", sans-serif;
    color: var(--white);
    line-height: 1;
  }
  .contact-phone { left: 200px; top: 300px; }
  .contact-email { left: 192px; top: 383px; }
  .contact-phone .contact-text { font-size: 54px; margin-left: 34px; letter-spacing: 1px; }
  .contact-email .contact-text { font-size: 46px; margin-left: 60px; }
  .icon { display: block; }
</style>
</head>
<body>
<div class="canvas">
  <section class="banner">
    <div class="banner-backdrop" role="img" aria-label="Abstract energetic background of red and blue light streaks, lightning and starry deep space"></div>
    <div class="turntable-photo" role="img" aria-label="Photo of a DJ mixer with red turntables"></div>

    <h1 class="logo-name" style="margin:0;font-weight:400;">DJ VAZ</h1>
    <p class="tagline" style="margin:0;">DJ-SERVICE-RENTALS</p>

    <div class="contact contact-phone">
      <svg class="icon" width="40" height="58" viewBox="0 0 40 58" aria-hidden="true">
        <rect x="2" y="2" width="36" height="54" rx="4" fill="none" stroke="#fff" stroke-width="3"/>
        <line x1="2" y1="44" x2="38" y2="44" stroke="#fff" stroke-width="3"/>
        <rect x="13" y="48" width="14" height="4" rx="1" fill="#fff"/>
      </svg>
      <span class="contact-text">555.014.2368</span>
    </div>

    <div class="contact contact-email">
      <svg class="icon" width="54" height="36" viewBox="0 0 54 36" aria-hidden="true">
        <rect x="2" y="2" width="50" height="32" fill="none" stroke="#fff" stroke-width="2.5"/>
        <polyline points="2,2 27,22 52,2" fill="none" stroke="#fff" stroke-width="2.5"/>
        <line x1="2" y1="34" x2="21" y2="17" stroke="#fff" stroke-width="2.5"/>
        <line x1="52" y1="34" x2="33" y2="17" stroke="#fff" stroke-width="2.5"/>
      </svg>
      <span class="contact-text">DJ@DJVAZ.net</span>
    </div>
  </section>
</div>
</body>
</html>
```